Minimalist Professional Business Card Design

We will be revamping our marketing materials: Business cards, Website and Catalogs.
Our Overall Design direction is to have a Minimalist artwork with Professionalism and Premium feel. The revamp starts with the new business card design followed by the others. Thus the designer whom work is selected for this job will likely to follow through with the subsequent jobs.

Target Market(s)

Upscale

Industry/Entity Type

Manufacturing

Contact Information for Business Card

For the Business Cards, the following are required:
. Minimalist yet Professional and Premium Feel
. Background Colors: white and / or light pastel yellow and if needed to smoothen the yellow, the light grey can be incorporated. We are changing our corporate bright yellow to either one of the three alternatives:
1. Soylant yellow CMYK (1%, 0%, 52%, 3%)
2. Popcorn yellow CMYK (0%, 0%, 33%, 0%)
3. Papaya yellow CMYK (0%, 0%, 51%, 0%)

Information to be inputed in the business cards:

Name: Ravel Amwerdi
Position: Managing Director

Company's name: Brolvane Valves Pte. Ltd.
Address: 412 Telbrook Lane #07-09K
Singapore 731852
Tel: (65) 6281 9046
Fax: (65) 6287 1149
Email: ravel@brolvanevalves.example
Website: www.brolvanevalves.example
Skype: Brolvane.Valves
Whatsapp/ Line/ Viber/ WeChat: (65) 9827 6013

Company's Logo
Company's Slogan
Two product photos placed side by side (if this gets into the way of the design, it is OK not to include them)

Font styles to use
Serif

Colors
ffffff

Requirements
Must have
• Minimalist
Should not have
• Messy, crowded, playful

```html
<!DOCTYPE html>
<html lang="en">
<head>
<meta charset="utf-8">
<title>Brolvane Valves – Business Card</title>
<link href="https://fonts.googleapis.com/css2?family=Lato:wght@400;700&display=swap" rel="stylesheet">
<style>
  :root {
    --page: #ecebe6;
    --card-yellow: #fdf79c;
    --card-white: #ffffff;
    --ink: #4a4a4a;
    --ink-soft: #6b6b6b;
    --band-grey: #5c5c5c;
    --photo-light: #f2f2f2;
    --photo-mid: #c9c9c9;
  }
  * { box-sizing: border-box; margin: 0; padding: 0; }
  html, body { width: 1200px; height: 1200px; overflow: hidden; }
  body {
    background: var(--page);
    font-family: "Lato", sans-serif;
    color: var(--ink);
    display: flex;
    flex-direction: column;
    align-items: center;
    justify-content: center;
    gap: 56px;
  }
  .card {
    width: 900px;
    height: 514px;
    position: relative;
    overflow: hidden;
    box-shadow: 0 6px 18px rgba(0,0,0,0.12);
  }
  /* front */
  .card-front {
    background: var(--card-yellow);
    display: flex;
    flex-direction: column;
    align-items: center;
    justify-content: center;
    gap: 22px;
  }
  .brand-mark {
    width: 120px; height: 120px;
    border-radius: 50%;
    border: 14px solid var(--ink);
  }
  .brand-name {
    font-weight: 700;
    font-size: 64px;
    letter-spacing: 6px;
    color: var(--ink);
  }
  /* back */
  .card-back { background: var(--card-white); }
  .product-photos {
    position: absolute;
    left: 70px; top: 60px;
    display: flex; gap: 40px;
  }
  .product-photo {
    width: 120px; height: 390px;
    border-radius: 10px;
    background: linear-gradient(90deg, var(--photo-mid), var(--photo-light) 45%, var(--photo-mid));
  }
  .details {
    position: absolute;
    left: 400px; top: 40px; right: 40px;
  }
  .details-brand {
    display: flex; align-items: center; gap: 12px;
    justify-content: center;
    margin-left: -40px;
  }
  .details-brand .brand-mark { width: 54px; height: 54px; border-width: 6px; }
  .details-brand .brand-name { font-size: 30px; letter-spacing: 3px; }
  .person { text-align: center; margin: 20px 0 0 -40px; }
  .person-name { font-weight: 700; font-size: 24px; }
  .person-title { font-size: 15px; color: var(--ink-soft); margin-top: 2px; }
  .company { font-weight: 700; font-size: 20px; margin-top: 26px; }
  .contact-columns {
    display: flex; gap: 30px; margin-top: 14px;
  }
  .contact-list { list-style: none; font-size: 16px; }
  .contact-list li {
    display: flex; align-items: flex-start; gap: 10px;
    margin-bottom: 9px; line-height: 1.3;
  }
  .contact-list li.strong { font-weight: 700; }
  .contact-list li.indent { padding-left: 28px; }
  .icon {
    flex: 0 0 18px; width: 18px; height: 18px;
    background: var(--ink); border-radius: 2px;
    display: flex; align-items: center; justify-content: center;
    margin-top: 1px;
  }
  .icon svg { width: 12px; height: 12px; }
  .chat-dots { display: inline-flex; gap: 4px; margin-left: 10px; vertical-align: middle; }
  .chat-dots span { width: 11px; height: 11px; border-radius: 50%; background: var(--ink); display: inline-block; }
  .band-grey {
    position: absolute; left: 0; bottom: 0;
    width: 52%; height: 14px; background: var(--band-grey);
  }
  .band-yellow {
    position: absolute; right: 0; bottom: 0;
    width: 48%; height: 30px; background: var(--card-yellow);
  }
</style>
</head>
<body>
  <section class="card card-front">
    <div class="brand-mark"></div>
    <div class="brand-name">BROLVANE</div>
  </section>

  <section class="card card-back">
    <div class="product-photos">
      <div class="product-photo" role="img" aria-label="Product photo: stainless steel valve unit with ribbed body"></div>
      <div class="product-photo" role="img" aria-label="Product photo: stainless steel cylindrical motor housing"></div>
    </div>

    <div class="details">
      <div class="details-brand">
        <div class="brand-mark"></div>
        <div class="brand-name">BROLVANE</div>
      </div>
      <div class="person">
        <div class="person-name">Ravel Amwerdi</div>
        <div class="person-title">Managing Director</div>
      </div>
      <div class="company">Brolvane Valves Pte. Ltd.</div>
      <div class="contact-columns">
        <ul class="contact-list">
          <li class="strong"><span class="icon"><svg viewBox="0 0 12 12"><path d="M2 1h2l1 3-1.5 1a6 6 0 0 0 3.5 3.5L8 7l3 1v2a1 1 0 0 1-1 1A9 9 0 0 1 1 2a1 1 0 0 1 1-1z" fill="#fff"/></svg></span>(65) 6281 9046</li>
          <li><span class="icon"><svg viewBox="0 0 12 12"><rect x="2" y="5" width="8" height="5" fill="#fff"/><rect x="3.5" y="1.5" width="5" height="3" fill="#fff"/></svg></span>(65) 6287 1149</li>
          <li><span class="icon"><svg viewBox="0 0 12 12"><path d="M6 1.5 1.5 6h1.5v4.5h6V6h1.5z" fill="#fff"/></svg></span>412 Telbrook Lane<br>#07-09K, Singapore 731852</li>
        </ul>
        <ul class="contact-list">
          <li><span class="icon"><svg viewBox="0 0 12 12"><rect x="1.5" y="3" width="9" height="6" fill="none" stroke="#fff"/><path d="M1.5 3 6 6.5 10.5 3" fill="none" stroke="#fff"/></svg></span>ravel@brolvanevalves.example</li>
          <li><span class="icon"><svg viewBox="0 0 12 12"><circle cx="6" cy="6" r="4.2" fill="none" stroke="#fff"/><path d="M1.8 6h8.4M6 1.8v8.4" stroke="#fff"/></svg></span>www.brolvanevalves.example</li>
          <li><span class="icon"><svg viewBox="0 0 12 12"><circle cx="6" cy="6" r="3.8" fill="#fff"/></svg></span>Brolvane.Valves</li>
          <li class="indent">(65) 9827 6013<span class="chat-dots"><span></span><span></span><span></span><span></span></span></li>
        </ul>
      </div>
    </div>

    <div class="band-grey"></div>
    <div class="band-yellow"></div>
  </section>
</body>
</html>
```